Dravetti Business Cards

We need a business card design for Dravetti Mining.

This is a B2B company that buys and sells large machinery tires within the coal mining industry. The design should the strong, crisp and masculine. I have uploaded the company logo and rough mock-up of what the back of the card should look like. the front of the card should have the same look/feel as the back. I need editable templates for both the front and the back of the card.

Color scheme should be grey/green/black

Contact information to include on the card:
Name: Owen Pellsworth
Title: Managing Director
Phone: 972-555-0143
Address: 3157 Brantley #5 Dallas, TX 75209
Email: Owen@Dravetti-example.com

I am also opening a contest for letterhead design. If you submit a business card design, please also submit a letterhead design with the same look/feel. The winner of the business card design will also will the letter head and be paid for both.

Target Market(s)

Procurement men/women in the coal mining industry

Industry/Entity Type

Coal Mining

```html
<!DOCTYPE html>
<html lang="en">
<head>
<meta charset="utf-8">
<title>Dravetti Mining – Business Card</title>
<link rel="stylesheet" href="https://fonts.googleapis.com/css2?family=Arimo:wght@400;600;700&display=swap">
<style>
  :root {
    --page-bg: #ffffff;
    --card-bg: #ffffff;
    --card-edge: #1a1a1a;
    --ink-grey: #58595b;
    --brand-green: #62a744;
    --soft-green: #b5d48d;
    --on-green: #ffffff;
  }
  * { margin: 0; padding: 0; box-sizing: border-box; }
  html, body {
    width: 1200px; height: 1000px; overflow: hidden;
    background: var(--page-bg);
    font-family: "Arimo", Helvetica, Arial, sans-serif;
  }
  .business-card {
    position: absolute; left: 76px; top: 201px;
    width: 1048px; height: 597px;
    background: var(--card-bg);
    border: 1.5px solid var(--card-edge);
    box-shadow: 6px 8px 10px rgba(0,0,0,0.22);
    overflow: hidden;
  }
  .address-panel {
    position: absolute; left: 674px; top: 0;
    width: 374px; height: 195px;
    background: var(--brand-green);
    color: var(--on-green);
    padding: 56px 0 0 46px;
    font-size: 23px; line-height: 28px;
  }
  .accent-panel {
    position: absolute; left: 674px; top: 198px;
    width: 374px; height: 400px;
    background: var(--soft-green);
  }
  .header-rule {
    position: absolute; left: 0; top: 194px;
    width: 674px; height: 4px;
    background: var(--brand-green);
  }
  .brand-lockup {
    position: absolute; left: 68px; top: 55px;
    display: flex; align-items: center; gap: 26px;
  }
  .brand-square {
    width: 86px; height: 86px; background: var(--brand-green);
  }
  .brand-name {
    color: var(--ink-grey);
    font-weight: 700; font-size: 52px; letter-spacing: 1px;
    line-height: 1;
  }
  .holder {
    position: absolute; left: 68px; top: 306px;
    color: var(--ink-grey);
  }
  .holder-name { font-size: 33px; font-weight: 600; line-height: 44px; }
  .holder-title { font-size: 25px; line-height: 36px; }
  .contact {
    position: absolute; left: 68px; top: 478px;
    color: var(--ink-grey);
    font-size: 26px; line-height: 36px;
  }
</style>
</head>
<body>
  <div class="business-card">
    <div class="brand-lockup">
      <div class="brand-square"></div>
      <div class="brand-name">DRAVETTI MINING</div>
    </div>
    <div class="header-rule"></div>

    <div class="address-panel">
      <p>3157 Brantley #5</p>
      <p>Dallas, TX 75209</p>
      <p>www.dravetti-example.com</p>
    </div>
    <div class="accent-panel"></div>

    <div class="holder">
      <p class="holder-name">Owen Pellsworth</p>
      <p class="holder-title">Managing Director</p>
    </div>

    <div class="contact">
      <p>(972) 555-0143</p>
      <p>Owen@Dravetti-example.com</p>
    </div>
  </div>
</body>
</html>
```